Flower delivery business needs sales brochure

I have a courier business that specialises in same-day flower deliveries; I want to make a single page A4 sales brochure (folded to DL) to give to our potential customers.
The company website is petalvanto.com, this will give an idea of who we are and what we do, as well as some graphics and colours that we use.
When opened, the inside A4 space of the brochure will be a pricelist, so the entire page will be an excel table with delivery locations and prices; we will add the prices ourselves later, so ideally the inside will be a background of some sort that won't obstruct text. Maybe light/transparent flowers and a background colour?
The front of the DL brochure should be mostly a title page, so business name, phone number, a graphic?
The first inside page should relate to our service, there's a lot of info on our website that you could use, so same day delivery, 10:30 and 2:30 pick-up times, established over 10 years ago, air-conditioned vans, delivery to 300+ suburbs.
The back page would be contact details and maybe a summary of the key points of the 'about us' section of the website.

Industry/Entity Type

Business

```html
<!DOCTYPE html>
<html lang="en">
<head>
<meta charset="utf-8">
<title>Petal Vanto – Florist Delivery Service Brochure</title>
<link href="https://fonts.googleapis.com/css2?family=Arimo:wght@400;700&family=Great+Vibes&family=Montserrat:wght@500;700&display=swap" rel="stylesheet">
<style>
  :root{
    --stage:#e4e4e4;
    --cream:#f8f1dd;
    --beige:#ece4d1;
    --green:#5a9a2c;
    --green-light:#7cb342;
    --green-dot:#9ccc65;
    --orange:#f08a24;
    --orange-dark:#e07412;
    --yellow:#f2b72a;
    --ink:#4a4035;
    --brown:#8a5a2b;
    --white:#ffffff;
  }
  *{box-sizing:border-box;margin:0;padding:0}
  html,body{width:1200px;height:855px;overflow:hidden;background:var(--stage)}
  .brochure{position:absolute;left:30px;top:28px;width:1140px;height:800px;display:flex;box-shadow:0 6px 24px rgba(0,0,0,.18)}
  .panel{position:relative;width:380px;height:800px;overflow:hidden}
  .panel--service{background:var(--cream)}
  .panel--contact{background:var(--beige);border-left:1px solid rgba(0,0,0,.06)}
  .panel--cover{background:var(--orange);border-left:1px solid rgba(0,0,0,.08)}

  .green-wave{position:absolute;left:0;bottom:0;width:100%;height:150px}

  /* service panel */
  .service-title{position:absolute;left:40px;top:56px;font-family:"Great Vibes",cursive;font-size:44px;color:var(--green);font-weight:400;line-height:1.1}
  .service-copy{position:absolute;left:40px;top:126px;width:300px;font-family:"Arimo",sans-serif;font-size:12.5px;line-height:1.32;color:var(--ink)}
  .service-copy p{margin-bottom:12px}
  .service-quote{position:absolute;left:40px;top:378px;width:300px;font-family:"Great Vibes",cursive;font-size:22px;line-height:1.12;color:var(--green)}
  .phone-pill{position:absolute;left:40px;top:462px;width:215px;height:40px;border-radius:0 20px 20px 0;background:var(--yellow);display:flex;align-items:center;gap:12px;padding-left:18px;font-family:"Arimo",sans-serif;font-weight:700;font-size:21px;color:var(--white)}
  .phone-pill svg{width:20px;height:20px}
  .courier-photo{position:absolute;left:30px;top:520px;width:225px;height:230px;border-radius:110px 110px 0 0;background:linear-gradient(180deg,#d8c4a2 0%,#b89a70 55%,#c0392b 100%);opacity:.9}
  .badge{position:absolute;left:228px;top:598px;width:124px;height:124px;border-radius:50%;background:var(--yellow);border:3px solid var(--white);box-shadow:0 0 0 2px var(--yellow);display:flex;align-items:center;justify-content:center;text-align:center;font-family:"Montserrat",sans-serif;font-weight:500;font-size:14.5px;line-height:1.15;color:var(--white);transform:rotate(-20deg)}

  /* contact panel */
  .bike-photo{position:absolute;left:118px;top:28px;width:150px;height:150px;border-radius:50%;border:5px solid var(--white);background:radial-gradient(circle at 40% 35%,#f4f1ee 0%,#cfd6d2 60%,#9fb3a8 100%);box-shadow:0 2px 6px rgba(0,0,0,.2)}
  .brand{position:absolute;left:0;width:100%;display:flex;align-items:center;justify-content:center;gap:12px}
  .brand__mark{width:34px;height:34px;border-radius:50%;background:var(--orange-dark)}
  .brand__name{font-family:"Arimo",sans-serif;font-weight:700;font-size:34px;letter-spacing:1px;text-transform:uppercase}
  .contact-brand{top:205px}
  .contact-brand .brand__name{color:var(--green)}
  .tagline{position:absolute;left:0;width:100%;text-align:center;font-family:"Great Vibes",cursive;font-size:24px}
  .contact-tagline{top:248px;color:var(--brown)}
  .dotted{position:absolute;left:40px;width:300px;border-top:2px dotted var(--orange)}
  .contact-details{position:absolute;left:0;top:300px;width:100%;text-align:center;font-family:"Arimo",sans-serif;font-size:12.5px;line-height:1.45;color:var(--ink)}
  .testimonial{position:absolute;left:40px;top:372px;width:300px;text-align:center;font-family:"Great Vibes",cursive;font-size:17px;line-height:1.3;color:var(--ink)}
  .testimonial__mark{color:var(--yellow);font-family:"Arimo",sans-serif;font-size:18px}
  .testimonial__source{position:absolute;left:0;top:470px;width:100%;text-align:center;font-family:"Great Vibes",cursive;font-size:19px;color:var(--ink)}
  .snapshot{position:absolute;border:5px solid var(--white);box-shadow:0 3px 8px rgba(0,0,0,.25)}
  .snapshot--street{left:30px;top:540px;width:180px;height:120px;transform:rotate(-4deg);background:linear-gradient(135deg,#c9b99a,#7f8f6a)}
  .snapshot--couple{left:198px;top:548px;width:165px;height:115px;transform:rotate(3deg);background:linear-gradient(135deg,#e9dfd5,#c79b82)}

  /* cover panel */
  .bouquet-photo{position:absolute;left:0;top:0;width:380px;height:470px;background:linear-gradient(160deg,#6b5a48 0%,#c9a59a 35%,#f2d6da 55%,#8a9a6a 80%,#5c4a3a 100%)}
  .cover-curve{position:absolute;left:0;top:380px;width:380px;height:110px}
  .cover-band{position:absolute;left:0;top:470px;width:380px;height:330px;background:linear-gradient(180deg,var(--orange) 0%,var(--orange-dark) 100%)}
  .cover-dot{position:absolute;left:170px;top:500px;width:40px;height:40px;border-radius:50%;background:#d9431e}
  .cover-brand{top:560px}
  .cover-brand .brand__name{color:var(--white);font-size:36px}
  .cover-tagline{top:606px;color:var(--white);font-size:26px}
  .cover-web{position:absolute;left:0;top:650px;width:100%;text-align:center;font-family:"Arimo",sans-serif;font-size:14px;color:var(--white);letter-spacing:.5px}
</style>
</head>
<body>
<div class="brochure">

  <section class="panel panel--service">
    <h2 class="service-title">Delivery Service</h2>
    <div class="service-copy">
      <p>Petal Vanto Pty Ltd is a courier company that specializes in the delivery of flowers and gifts. We offer a same day courier service for the florist &amp; gift retail and wholesale market, and deliver to over 300 suburbs throughout the Brisbane Metropolitan region.</p>
      <p>We have been in the business for over 10 years, and are very focused on delivering the best customer service possible.</p>
      <p>All our air conditioned vans are specially equipped for the delivery of flowers and are presented to your customer by one of our easily recognizable and professional uniformed drivers.</p>
    </div>
    <p class="service-quote">We understand that its not just the gift of flowers, but the emotion that we are transporting!</p>
    <div class="phone-pill">
      <svg viewBox="0 0 24 24" aria-hidden="true"><path fill="#fff" d="M6.6 10.8a15.1 15.1 0 0 0 6.6 6.6l2.2-2.2c.3-.3.7-.4 1-.2 1.1.4 2.3.6 3.6.6.6 0 1 .4 1 1V20c0 .6-.4 1-1 1C10.6 21 3 13.4 3 4c0-.6.4-1 1-1h3.5c.6 0 1 .4 1 1 0 1.3.2 2.5.6 3.6.1.3 0 .7-.2 1z"/></svg>
      0400 555 217
    </div>
    <div class="courier-photo" role="img" aria-label="Photo of a smiling delivery driver in uniform holding a bouquet of red roses and a clipboard"></div>
    <svg class="green-wave" viewBox="0 0 380 150" preserveAspectRatio="none" aria-hidden="true">
      <defs><pattern id="dotsA" width="10" height="10" patternUnits="userSpaceOnUse"><circle cx="5" cy="5" r="1.3" fill="var(--green-dot)"/></pattern></defs>
      <path d="M0 60 C120 110 260 60 380 20 L380 150 L0 150 Z" fill="var(--green-light)"/>
      <path d="M0 60 C120 110 260 60 380 20 L380 150 L0 150 Z" fill="url(#dotsA)"/>
    </svg>
    <div class="badge">SAME DAY<br>DELIVERY<br>SERVICE</div>
  </section>

  <section class="panel panel--contact">
    <div class="bike-photo" role="img" aria-label="Round photo of a vintage bicycle with a basket of flowers"></div>
    <div class="brand contact-brand"><span class="brand__mark"></span><span class="brand__name">Petal Vanto</span></div>
    <p class="tagline contact-tagline">Florist Delivery Service</p>
    <div class="dotted" style="top:288px"></div>
    <div class="contact-details">
      0400 555 217<br>
      PO Box 4410 Brookfield DC QLD, 4069<br>
      (9am-5pm Mon-Fri &amp; 9am-3pm Sat)
    </div>
    <div class="dotted" style="top:358px"></div>
    <p class="testimonial"><span class="testimonial__mark">“</span>Petal Vanto deliver the perfect service to support our business. Fernleaf Flowers is very happy with their consistent high level of service and flexibility. We definitely recommend Petal Vanto as a premier flower courier.<span class="testimonial__mark">”</span></p>
    <p class="testimonial__source">Fernleaf Flowers &amp; Gifts</p>
    <svg class="green-wave" viewBox="0 0 380 150" preserveAspectRatio="none" aria-hidden="true">
      <defs><pattern id="dotsB" width="10" height="10" patternUnits="userSpaceOnUse"><circle cx="5" cy="5" r="1.3" fill="var(--green-dot)"/></pattern></defs>
      <path d="M0 20 C120 -5 260 10 380 -10 L380 150 L0 150 Z" fill="var(--green-light)"/>
      <path d="M0 20 C120 -5 260 10 380 -10 L380 150 L0 150 Z" fill="url(#dotsB)"/>
    </svg>
    <div class="snapshot snapshot--street" role="img" aria-label="Photo of a couple embracing on a city street"></div>
    <div class="snapshot snapshot--couple" role="img" aria-label="Photo of a couple with a bouquet of flowers"></div>
  </section>

  <section class="panel panel--cover">
    <div class="bouquet-photo" role="img" aria-label="Photo of lush arrangements of pink roses, white hydrangeas and green foliage"></div>
    <svg class="cover-curve" viewBox="0 0 380 110" preserveAspectRatio="none" aria-hidden="true">
      <path d="M0 60 C120 110 260 110 380 0 L380 110 L0 110 Z" fill="var(--orange)"/>
    </svg>
    <div class="cover-band"></div>
    <div class="cover-dot"></div>
    <div class="brand cover-brand"><span class="brand__name">Petal Vanto</span></div>
    <p class="tagline cover-tagline">Florist Delivery Service</p>
    <p class="cover-web">www.petalvanto.com</p>
  </section>

</div>
</body>
</html>
```